Personal Development Brand Needs a Workbook Cover Design

We need a clean and sleek cover design for our A4-Sized workbook called the "Lantern Path Journal Set"

There's around 90 pages in the workbook, if that matters for the spine.

Necessary Elements on the Front Cover:

- Logo
- Title: Keen Crest Lantern Path Journal
- Subtitle: A Simple Workbook to Track Your Transformation
- Author Name: Dorian Pellow

Elements on Back Cover:

- The Keen Crest Charter

```html
<!DOCTYPE html>
<html lang="en">
<head>
<meta charset="utf-8">
<title>Keen Crest Lantern Path Journal – Cover</title>
<link rel="stylesheet" href="https://fonts.googleapis.com/css2?family=Roboto+Condensed:wght@700;800&family=Roboto:wght@900&family=Old+Standard+TT:wght@400;700&family=Cinzel:wght@700&display=swap">
<style>
  :root {
    --ink: #000000;
    --spine: #2b2b2b;
    --signal-red: #e13b2d;
    --label-red: #b3272b;
    --slate: #36414c;
    --silver-hi: #ffffff;
    --silver-lo: #a9a9a9;
    --pale: #d9d9d9;
    --paper: #ffffff;
    --box-text: #2a1512;
  }
  * { margin: 0; padding: 0; box-sizing: border-box; }
  html, body { width: 1200px; height: 870px; overflow: hidden; background: var(--ink); }
  .cover-spread { position: relative; width: 1200px; height: 870px; background: var(--ink); }

  /* Back cover */
  .back-cover { position: absolute; left: 0; top: 0; width: 580px; height: 870px; background: var(--ink); }
  .charter-label {
    position: absolute; left: 56px; top: 98px; width: 470px; height: 71px;
    background: var(--label-red); color: var(--paper);
    font: 800 45px/71px "Roboto Condensed", sans-serif; letter-spacing: -1.6px;
    text-align: center; white-space: nowrap;
  }
  .charter-line {
    position: absolute; left: 0; width: 582px; text-align: center; color: var(--paper);
    font: 800 32px/42px "Roboto Condensed", sans-serif; letter-spacing: -1.2px;
  }

  /* Spine */
  .spine { position: absolute; left: 580px; top: 0; width: 39px; height: 870px; background: var(--spine); }

  /* Front cover */
  .front-cover { position: absolute; left: 619px; top: 0; width: 581px; height: 870px; background: var(--ink); }
  .brand-mark {
    position: absolute; left: 33px; top: 70px; width: 522px; height: 70px;
    display: flex; align-items: center; justify-content: center; gap: 18px;
  }
  .brand-square { width: 34px; height: 34px; background: var(--pale); }
  .brand-name {
    color: var(--pale); font: 700 54px/70px "Roboto Condensed", sans-serif; letter-spacing: 0;
  }
  .red-rule { position: absolute; left: 33px; width: 522px; height: 24px; background: var(--signal-red); }
  .rule-top { top: 198px; }
  .rule-bottom { top: 372px; }
  .title-main {
    position: absolute; left: 0; top: 252px; width: 581px; text-align: center;
    font: 900 84px/92px "Roboto", sans-serif; letter-spacing: -1px;
    background: linear-gradient(180deg, var(--silver-hi) 0%, var(--pale) 50%, var(--silver-lo) 100%);
    -webkit-background-clip: text; background-clip: text; color: transparent;
  }
  .title-upper {
    position: absolute; left: 0; top: 408px; width: 581px; text-align: center;
    color: var(--pale); font: 400 34px/36px "Old Standard TT", serif; letter-spacing: -0.5px;
  }
  .title-lower {
    position: absolute; left: 0; top: 442px; width: 581px; text-align: center;
    color: var(--signal-red); font: 400 76px/78px "Old Standard TT", serif; letter-spacing: -1px;
  }
  .subtitle-box {
    position: absolute; left: 0; top: 563px; width: 581px; height: 185px;
    background: var(--signal-red); color: var(--box-text);
    display: flex; flex-direction: column; justify-content: center; align-items: center;
    font: 400 27px/37px "Old Standard TT", serif; letter-spacing: -0.6px; text-align: center;
    text-transform: uppercase;
  }
  .subtitle-box span { display: block; transform: scaleX(0.82); white-space: nowrap; }
  .author-name {
    position: absolute; left: 0; top: 796px; width: 581px; text-align: center;
    color: var(--paper); font: 700 35px/42px "Cinzel", serif; letter-spacing: 5px;
    white-space: nowrap;
  }
</style>
</head>
<body>
<main class="cover-spread">
  <section class="back-cover" aria-label="Back cover">
    <h2 class="charter-label">The Keen Crest Charter</h2>
    <p class="charter-line" style="top:207px">We do things that matter.</p>
    <p class="charter-line" style="top:293px">We are skeptical of our limits.</p>
    <p class="charter-line" style="top:379px">We don’t fear mistakes,<br>only mediocrity.</p>
    <p class="charter-line" style="top:506px">We don’t just think positive<br>thoughts, we act on them.</p>
    <p class="charter-line" style="top:635px">We know our most important<br>skill is the ability to dream<br>beyond our current abilities.</p>
  </section>

  <div class="spine" aria-hidden="true"></div>

  <section class="front-cover" aria-label="Front cover">
    <div class="brand-mark">
      <span class="brand-square" aria-hidden="true"></span>
      <span class="brand-name">Keen Crest</span>
    </div>
    <div class="red-rule rule-top"></div>
    <h1 class="title-main">KEEN CREST</h1>
    <div class="red-rule rule-bottom"></div>
    <p class="title-upper">LANTERN PATH</p>
    <p class="title-lower">JOURNAL</p>
    <div class="subtitle-box">
      <span>A Simple</span>
      <span>Workbook</span>
      <span>to Track Your Transformation</span>
    </div>
    <p class="author-name">DORIAN PELLOW</p>
  </section>
</main>
</body>
</html>
```